Real Estate For Sale Sign

I need to design a for sale sign. It needs to include The following information
Logo: Attached
Name: Corinne Vasquel,
Company Name: Gilded Harbor Real Estate,
Phone Number: 503-841-2096
BRE Licence Number 04817359 (Can Be small)
Sign size 24x30

I am not sure about including my website but I would like to see options with it. www.gildedharbor-example.com
Updates

Target Market(s)

Potential Buyers or Sellers of Real Estate. Must be easy to read.

Industry/Entity Type

Real Estate

Requirements
Must have
• I want it to feel luxurious and sharp.

```html
<!DOCTYPE html>
<html lang="en">
<head>
<meta charset="utf-8">
<title>Gilded Harbor Real Estate – For Sale Sign</title>
<link rel="stylesheet" href="https://fonts.googleapis.com/css2?family=Open+Sans:wght@700&family=Roboto+Condensed:wght@700&display=swap">
<style>
  :root {
    --backdrop: #b8c8c7;
    --panel-white: #ffffff;
    --header-strip: #6f7f7e;
    --brand-blue: #0033a8;
    --brand-navy: #00163f;
    --text-white: #ffffff;
    --mark-blue: #2f8fe0;
  }
  html, body {
    margin: 0;
    padding: 0;
    width: 1200px;
    height: 900px;
    overflow: hidden;
    background: var(--backdrop);
  }
  .canvas {
    position: relative;
    width: 1200px;
    height: 900px;
  }
  .sign {
    position: absolute;
    left: 372px;
    top: 118px;
    width: 456px;
    height: 460px;
    display: flex;
    flex-direction: column;
  }
  .sign__strip {
    height: 14px;
    background: var(--header-strip);
  }
  .sign__header {
    position: relative;
    height: 224px;
    background: var(--panel-white);
  }
  .brand {
    position: absolute;
    left: 18px;
    top: 28px;
    display: flex;
    align-items: center;
    gap: 18px;
  }
  .brand__circle {
    width: 104px;
    height: 104px;
    border-radius: 50%;
    border: 6px solid var(--mark-blue);
    box-sizing: border-box;
  }
  .brand__name {
    font-family: "Open Sans", sans-serif;
    font-weight: 700;
    color: var(--brand-blue);
    font-size: 26px;
    line-height: 1.15;
    letter-spacing: 0.5px;
    text-transform: uppercase;
  }
  .brand__name small {
    display: block;
    font-size: 13px;
    letter-spacing: 4px;
    margin-top: 4px;
  }
  .agent-name {
    position: absolute;
    left: 190px;
    top: 170px;
    margin: 0;
    font-family: "Open Sans", sans-serif;
    font-weight: 700;
    font-size: 28px;
    color: var(--brand-blue);
    white-space: nowrap;
  }
  .sign__band {
    height: 200px;
    background: var(--brand-blue);
    color: var(--text-white);
    font-family: "Roboto Condensed", sans-serif;
    font-weight: 700;
    text-align: center;
    position: relative;
  }
  .band__title {
    position: absolute;
    left: 0; right: 0;
    top: 34px;
    font-size: 52px;
    line-height: 1;
    letter-spacing: 1px;
  }
  .band__phone {
    position: absolute;
    left: 0; right: 0;
    top: 102px;
    font-size: 52px;
    line-height: 1;
    letter-spacing: 1px;
  }
  .band__licence {
    position: absolute;
    left: 0; right: 0;
    top: 163px;
    font-size: 16px;
    line-height: 1;
  }
  .sign__footer {
    height: 22px;
    background: var(--brand-navy);
  }
</style>
</head>
<body>
<main class="canvas">
  <section class="sign" aria-label="For sale sign">
    <div class="sign__strip"></div>
    <header class="sign__header">
      <div class="brand">
        <span class="brand__circle" aria-hidden="true"></span>
        <span class="brand__name">Gilded Harbor<small>Real Estate</small></span>
      </div>
      <h1 class="agent-name">Corinne Vasquel</h1>
    </header>
    <div class="sign__band">
      <div class="band__title">FOR SALE</div>
      <div class="band__phone">503-841-2096</div>
      <div class="band__licence">04817359 BRE Licence Number</div>
    </div>
    <div class="sign__footer"></div>
  </section>
</main>
</body>
</html>
```